ちょっと急いでおりまして、
当方デザインをする時間がないので、
アウトソーシングしたいと思います。

文章、と構成だけを作りましたので、
宜しければ、お願い致します。

TAVELIA JAPAN で使用する、
お客さまにブランディングするための、
青嶺かやどり の パンフレットです。

PDFで、説明文を記載致しますので、
また見ておいて下さい。

画像素材も、添付させて頂きます。
「青嶺かやどり・かやたまご」を使うフォントは、
明朝体です。アウトラインしたデータも
添付いたします。それを活用下さい。

A4サイズ (裏・表)
両面カラーでで作っていただけると幸いです。

※もしかすると、A0サイズで引き伸ばしてつかうかもしれません。
どうぞよろしくお願い致します。

何か御不明な点がございましたら、お気軽に
ご質問ください。

当社青嶺かやどりの商品ページです。
参考にして下さい。
http://item.shopmarket-example.jp/poultry-hoshino/20004681/

青嶺かやどり協議会の ページです。
http://www.kayadori-example.com/
素材を添付いたします。レイヤーを使っておりますので、分解してください。
このページにある

の画像のような感じで、要約していただけると
幸いです。
画像を追加いたしました。
タイトルが、4Aに なってました。

すみません。A4ポスターです。
循環型の 111 のような 感じで、

ぐるっと 回る ように わかりやすく つくって頂けると幸いです。
かやどりの アニメーションデータは、

aiファイル イラストレーターの
かやたまご に 入っています。

レイヤーで組んでいますが、それを修正して作って下さい。
素材 画像を追加いたしました。
素材追加いたします。

111、222、333、444画像は、見本画像です。
イメージの参考になるかも?と思いまして、
かやどり からでる 副産物の 鶏糞堆肥もっこもこ の画像を 追加いたします。

裏側の、一番重要な情報を綺麗にまとめてくださりました。
そして、私達が やっていることに対して 共感頂けたことが大きかったです。
少し修正頂きたい部分がありますので、御連絡頂けると幸いです。

皆様 急な対応、ありがとうございます。
10件も御応募いただけるとは思っても居なかったのと、
そして、みなさんからの提案が本当に良かったので。
こちらとしても 悩ましかったです。
御提案くださった皆様。本当に、ありがとうございましたm(__)m

```html
<!DOCTYPE html>
<html lang="ja">
<head>
<meta charset="utf-8">
<title>青嶺かやどり かやたまご</title>
<link rel="stylesheet" href="https://fonts.googleapis.com/css2?family=Shippori+Mincho:wght@500;700;800&family=Noto+Sans+JP:wght@400;500;700&display=swap">
<style>
  :root{
    --paper:#fbf8f0;
    --ink:#2b2622;
    --ink-soft:#4a433c;
    --olive:#a8955a;
    --olive-light:#d9cfa8;
    --accent:#e07a2a;
    --photo-warm:#c9b79a;
    --photo-green:#9fae86;
    --chick:#f7f3ea;
    --chick-edge:#e6dcc0;
  }
  *{box-sizing:border-box;margin:0;padding:0}
  html,body{width:853px;height:1200px;overflow:hidden;background:var(--paper)}
  body{font-family:"Noto Sans JP",sans-serif;color:var(--ink);position:relative}
  .poster{position:relative;width:853px;height:1200px;background:var(--paper)}
  .abs{position:absolute}
  .vertical{writing-mode:vertical-rl;text-orientation:mixed}

  .title{font-family:"Shippori Mincho",serif;font-weight:800;font-size:74px;line-height:1;letter-spacing:4px;color:var(--ink)}
  .title-main{left:92px;top:40px}
  .title-sub{left:16px;top:150px}
  .title-region{font-size:60px}

  .tagline{left:176px;top:122px;width:84px;font-size:8.5px;line-height:1.45;color:var(--ink-soft)}
  .tagline strong{display:block;margin-top:6px;font-weight:700;font-size:9px}

  .origin-heading{left:738px;top:60px;font-family:"Shippori Mincho",serif;font-weight:800;font-size:30px;line-height:1.25;color:var(--accent);letter-spacing:2px}
  .origin-body{left:272px;top:58px;height:290px;width:450px;font-size:12.5px;line-height:1.95;color:var(--ink-soft);letter-spacing:1px}
  .origin-body p+p{margin-right:14px}

  .cycle-heading{left:290px;top:366px;width:520px;text-align:center;font-family:"Shippori Mincho",serif;font-weight:800;font-size:30px;letter-spacing:2px}
  .cycle-heading::before,.cycle-heading::after{content:"";display:inline-block;width:46px;height:2px;background:var(--olive);vertical-align:middle;margin:0 14px}

  .ring{left:230px;top:490px}
  .chick-art{left:285px;top:545px;width:270px;height:270px;border-radius:50%;background:radial-gradient(circle at 45% 45%,var(--chick) 50%,var(--chick-edge))}

  .step-num{font-family:"Shippori Mincho",serif;font-weight:800;font-size:58px;line-height:1;color:var(--olive)}
  .step-label{font-family:"Shippori Mincho",serif;font-weight:700;font-size:17px;line-height:1.35}
  .step-note{font-size:14px;font-weight:500;color:var(--ink-soft)}

  .side-text{font-size:11.5px;line-height:1.75;color:var(--ink-soft)}

  .photo{border-radius:2px}
  .photo-farmer{left:18px;top:962px;width:232px;height:222px;background:linear-gradient(160deg,var(--photo-green),var(--photo-warm))}
  .photo-compost{left:706px;top:982px;width:132px;height:204px;background:linear-gradient(180deg,#b49a74,#7c6448)}

  .farm-heading{left:264px;top:962px;width:230px;font-family:"Shippori Mincho",serif;font-weight:800;font-size:19px;line-height:1.35;color:var(--accent)}
  .farm-body{left:264px;top:1030px;width:236px;font-size:11px;line-height:1.75;color:var(--ink-soft)}
  .compost-body{left:530px;top:1000px;height:186px;width:160px;font-size:11.5px;line-height:1.85;color:var(--ink-soft)}
</style>
</head>
<body>
<main class="poster">

  <h1 class="title-block">
    <span class="abs vertical title title-main"><span class="title-region">青嶺</span>かやどり</span>
    <span class="abs vertical title title-sub">かやたまご</span>
  </h1>

  <p class="abs tagline">It is so delicious. You will be happy if you take it. Everyone says, "This is the great Chicken and Egg. Try it!"<strong>Aomine Kayadori Kayatamago</strong></p>

  <h2 class="abs vertical origin-heading">かやどりが<br>はじまった経緯</h2>
  <div class="abs vertical origin-body">
    <p>青嶺梅の産地である青嶺の里では、梅干しを作る過程で出る梅酢の使い道に長く悩んできました。</p>
    <p>そこで地元の養鶏農家と梅農家が手を取り合い、梅酢を鶏の餌に加える取り組みを始めました。</p>
    <p>その結果、元気に育つ鶏が生まれ、「青嶺かやどり」と名付けられました。その鶏が産む卵が「かやたまご」です。</p>
    <p>こうして地域の恵みを無駄なく活かす、かやどりの物語がはじまりました。</p>
  </div>

  <h2 class="abs cycle-heading">鶏糞堆肥「もっこもこ」</h2>

  <svg class="abs ring" width="380" height="380" viewBox="0 0 380 380" aria-hidden="true">
    <circle cx="190" cy="190" r="165" fill="none" stroke="var(--olive-light)" stroke-width="22"/>
    <circle cx="190" cy="190" r="165" fill="none" stroke="var(--olive)" stroke-width="4" stroke-dasharray="6 10"/>
    <polygon points="315.5,81.5 308.4,60.2 294.2,74.4" fill="var(--olive)"/>
    <polygon points="298.5,315.5 319.8,308.4 305.6,294.2" fill="var(--olive)"/>
    <polygon points="64.5,298.5 71.6,319.8 85.8,305.6" fill="var(--olive)"/>
    <polygon points="81.5,64.5 60.2,71.6 74.4,85.8" fill="var(--olive)"/>
  </svg>
  <div class="abs chick-art" role="img" aria-label="かやどりのキャラクターイラスト(ひよこと卵)"></div>

  <div class="abs" style="left:250px;top:428px"><span class="step-num">1</span></div>
  <p class="abs step-label" style="left:295px;top:438px;width:150px">青嶺かやどり<br>から「鶏糞」</p>

  <p class="abs step-note" style="left:140px;top:566px">1にもどります</p>

  <div class="abs" style="left:100px;top:636px"><span class="step-num">5</span></div>
  <p class="abs step-label" style="left:36px;top:704px;width:190px">かやどりの<br>餌用の梅酢ができる</p>

  <div class="abs" style="left:66px;top:822px"><span class="step-num">4</span></div>
  <p class="abs step-label" style="left:112px;top:812px;width:150px">梅農家が<br>もっこもこを使う</p>

  <div class="abs" style="left:604px;top:690px"><span class="step-num">2</span></div>
  <p class="abs step-label" style="left:650px;top:700px;width:180px">梅干作りから<br>「調味廃液」</p>

  <div class="abs" style="left:470px;top:866px"><span class="step-num">3</span></div>
  <p class="abs step-label" style="left:516px;top:876px;width:150px">『もっこもこ』<br>の誕生</p>

  <p class="abs side-text" style="left:618px;top:440px;width:220px">この鶏糞に、梅干作りで出る調味廃液を混ぜ合わせて発酵させます。じっくりと時間をかけることで、においの少ない、ふんわりとした堆肥に仕上がります。土にやさしく、梅の木を元気に育てます。</p>
  <p class="abs side-text" style="left:618px;top:780px;width:220px">このように、地域の中で生まれたものを地域に還す循環が続いています。堆肥で育った梅から梅酢が生まれ、ふたたび鶏の餌になります。</p>

  <div class="abs photo photo-farmer" role="img" aria-label="鶏を抱く養鶏農家の写真"></div>
  <h3 class="abs farm-heading">自然豊かな環境で<br>すくすく育ちました</h3>
  <p class="abs farm-body">山と海に囲まれた青嶺の里で、かやどりはのびのびと育てられています。梅酢入りの餌と澄んだ空気のなかで、健康な鶏とおいしい卵が生まれます。毎日の手間を惜しまず、ひとつひとつ大切に届けています。</p>

  <div class="abs vertical compost-body">発酵を重ねた堆肥は、手に取るとふかふかとやわらかく、梅畑の土をよみがえらせます。</div>
  <div class="abs photo photo-compost" role="img" aria-label="鶏糞堆肥もっこもこを手に取った写真"></div>

</main>
</body>
</html>
```